Need a business cards for a hair dressing salon.

Target Market(s)

Target woman for Hair cuts, bridal makeup, occasion, fashion makeup and etc.

Industry/Entity Type

Hair

Font styles to use
Serif
Script

Requirements
Must have
• - Business card to be memorable and recognizable

- Please include the following on the business card:
- Business name: Salon Marolin
- Name: Nilumi Jayasekara (Name Must be changeable)
- Occupation: Hair Dresser & Beautician
- Contact number: 04 731 6 CURL
- Email: mail@marolin.com.au
- Facebook (please use image): www.facebook.com/marolin.com.au
Nice to have
• Font Styles:
Business Name - Script
Other Text - Serif

```html
<!DOCTYPE html>
<html lang="en">
<head>
<meta charset="utf-8">
<title>Salon Marolin – Business Card</title>
<link rel="stylesheet" href="https://fonts.googleapis.com/css2?family=Questrial&display=swap">
<style>
  :root {
    --page: #ffffff;
    --band-dark: #1d2220;
    --band-dark-edge: #141817;
    --band-light: #d4d3d4;
    --gold: #c9a640;
    --ink: #111111;
    --ink-soft: #2a2a2a;
  }
  * { margin: 0; padding: 0; box-sizing: border-box; }
  html, body {
    width: 1200px;
    height: 718px;
    overflow: hidden;
    background: var(--page);
  }
  .card {
    position: absolute;
    left: 22px;
    top: 18px;
    width: 1156px;
    height: 676px;
  }
  .card__hero {
    position: absolute;
    left: 0; top: 0;
    width: 100%;
    height: 435px;
    background: radial-gradient(ellipse at 50% 45%, #27302d 0%, var(--band-dark) 55%, var(--band-dark-edge) 100%);
  }
  .brand-name {
    position: absolute;
    left: 0; right: 0;
    top: 162px;
    text-align: center;
    font-family: "Questrial", sans-serif;
    font-weight: 400;
    font-size: 104px;
    line-height: 1;
    letter-spacing: 4px;
    color: var(--gold);
  }
  .card__details {
    position: absolute;
    left: 0; top: 435px;
    width: 100%;
    height: 241px;
    background: var(--band-light);
  }
  .person {
    position: absolute;
    right: 630px;
    top: 75px;
    text-align: right;
    font-family: "Questrial", sans-serif;
  }
  .person__name {
    font-size: 37px;
    color: var(--ink);
    line-height: 1.1;
  }
  .person__role {
    margin-top: 10px;
    font-size: 20px;
    color: var(--ink-soft);
  }
  .divider {
    position: absolute;
    left: 551px;
    top: 54px;
    width: 3px;
    height: 135px;
    background: var(--gold);
  }
  .contacts {
    position: absolute;
    left: 578px;
    top: 58px;
    list-style: none;
    font-family: "Questrial", sans-serif;
    font-size: 21px;
    color: var(--ink);
  }
  .contacts__item {
    display: flex;
    align-items: center;
    height: 46px;
  }
  .contacts__icon {
    width: 32px;
    height: 32px;
    margin-right: 26px;
    flex: none;
  }
</style>
</head>
<body>
  <main class="card">
    <section class="card__hero" role="img" aria-label="Dark green damask floral pattern background">
      <h1 class="brand-name">Salon Marolin</h1>
    </section>
    <section class="card__details">
      <div class="person">
        <p class="person__name">Nilumi Jayasekara</p>
        <p class="person__role">Hair Dresser &amp; Beautician</p>
      </div>
      <div class="divider"></div>
      <ul class="contacts">
        <li class="contacts__item">
          <svg class="contacts__icon" viewBox="0 0 32 32" aria-hidden="true">
            <circle cx="16" cy="16" r="14" fill="none" stroke="#111" stroke-width="2"/>
            <path d="M11 9.5c1-.8 2-.6 2.6.4l1.3 2.2c.5.8.3 1.6-.4 2.1l-.9.6c.7 1.8 2 3.2 3.7 4l.7-.9c.5-.7 1.4-.8 2.1-.3l2.1 1.4c.9.6 1 1.7.2 2.5-1.2 1.3-3 1.7-4.7.8-3.5-1.8-6-4.6-7.3-8.3-.6-1.6-.3-3.4.6-4.5z" fill="#111"/>
          </svg>
          <span>04 731 6 CURL</span>
        </li>
        <li class="contacts__item">
          <svg class="contacts__icon" viewBox="0 0 32 32" aria-hidden="true">
            <circle cx="16" cy="16" r="14" fill="none" stroke="#111" stroke-width="2"/>
            <text x="16" y="21.5" text-anchor="middle" font-family="Questrial, sans-serif" font-size="17" fill="#111">@</text>
          </svg>
          <span>mail@marolin.com.au</span>
        </li>
        <li class="contacts__item">
          <svg class="contacts__icon" viewBox="0 0 32 32" aria-hidden="true">
            <circle cx="16" cy="16" r="14" fill="none" stroke="#111" stroke-width="2"/>
          </svg>
          <span>www.socialpage.net/marolin.com.au</span>
        </li>
      </ul>
    </section>
  </main>
</body>
</html>
```